DNN Website Design Project

We are going to recreate the website www.plorvenstudio.com. This is a DNN website. We like http://www.quilbarnhq.com/ and something like http://www.redstonequarryweb.com/

Look at plorvenstudio.com to see what we do, SMM, SEO and website development mostly. We have a number of video testimonials and want people to be able to contact us easily and have social media integration.

Target Market(s)

small and medium sized business owners, doctors, private practice professionals, lawyers, service pros (plumbers, electricians)

Industry/Entity Type

Media

```html
<!DOCTYPE html>
<html lang="en">
<head>
<meta charset="utf-8">
<title>Plorven Studio</title>
<link href="https://fonts.googleapis.com/css2?family=PT+Sans:wght@400;700&family=Oswald:wght@500&family=Roboto+Condensed:wght@400&display=swap" rel="stylesheet">
<style>
:root{
  --red:#c4070f;--red-dark:#a8060c;--navy:#0c1a3c;--ink:#333;--grey-bg:#e4e4e4;
  --light-bg:#ececec;--card-body:#3a3a3a;--beige:#efe6d3;--footer-dark:#1e1e1e;--link-gold:#f3c66a;
}
*{box-sizing:border-box;margin:0;padding:0}
html,body{width:754px;height:1200px;overflow:hidden}
body{position:relative;background:var(--grey-bg);font-family:"PT Sans",sans-serif;color:var(--ink)}
.abs{position:absolute}
.topline{left:0;top:0;width:754px;height:2px;background:var(--red)}
.brand{left:98px;top:6px;display:flex;align-items:center;gap:6px}
.brand-dot{width:48px;height:48px;border-radius:50%;background:var(--red)}
.brand-name{font-weight:700;font-size:15px;color:var(--red)}
.quote-btn{left:522px;top:2px;width:132px;height:20px;background:var(--red);color:#fff;font-size:9px;font-weight:700;display:flex;align-items:center;padding-left:12px;border-radius:0 0 4px 4px}
.quote-btn span{position:absolute;right:6px;top:3px;width:14px;height:14px;border-radius:50%;background:#fff}
.socials{left:521px;top:34px;display:flex;gap:7px}
.socials i{width:17px;height:17px;border-radius:50%;background:#8a8a8a;display:block}
.nav{left:0;top:58px;width:754px;height:27px;background:#dcdcdc;border-top:1px solid #cfcfcf}
.nav a{position:absolute;top:8px;font-size:9px;color:#222;text-decoration:none}
.nav a.active{color:var(--red)}
.nav b{position:absolute;top:6px;width:1px;height:15px;background:#c8c8c8}
.hero{left:0;top:85px;width:754px;height:249px;background:radial-gradient(ellipse at 60% 40%,#1e3470,var(--navy) 70%)}
.hero h1{left:98px;top:42px;font-family:"Oswald",sans-serif;font-size:19px;color:#fff;font-weight:500}
.hero p{left:98px;top:74px;width:190px;font-size:7.6px;line-height:12.8px;color:#fff}
.btn-red{background:var(--red);color:#fff;font-size:8.5px;display:flex;align-items:center;justify-content:center;border-radius:3px}
.tablet{left:302px;top:14px;width:352px;height:221px;border-radius:14px;background:linear-gradient(#2b2b2b,#0b0b0b);border:1px solid #555}
.screen{left:31px;top:27px;width:289px;height:162px;background:radial-gradient(circle at 55% 55%,#3c9bf5,#0a3f9c 75%)}
.dots{left:160px;top:200px;display:flex;gap:5px}
.dots i{width:7px;height:7px;border-radius:50%;background:var(--red);display:block}
.card{top:350px;width:130px;height:142px;background:var(--card-body)}
.card h3{height:29px;background:var(--red);color:#fff;font-family:"Roboto Condensed",sans-serif;font-weight:400;font-size:12.5px;text-align:center;line-height:29px;border-bottom:1px dotted #fff}
.card p{padding:9px 8px 0;font-size:6.6px;line-height:11.6px;color:#ddd;text-align:center}
.tag{position:absolute;left:0;top:116px;width:84px;height:16px;background:#fff;color:var(--red);font-family:"Roboto Condensed",sans-serif;font-size:9px;line-height:16px;padding-left:10px;clip-path:polygon(0 0,86% 0,100% 50%,86% 100%,0 100%)}
.tag.hot{background:var(--red);color:#fff}
.side-panel{left:0;top:492px;width:264px;height:282px;background:#ececec}
.sec-title{font-size:8.5px;font-weight:700;color:var(--red);text-transform:uppercase}
.svc-list{left:98px;top:522px;width:139px;list-style:none}
.svc-list li{height:17.4px;border-bottom:1px dotted #ccc;font-size:7.6px;line-height:17px;padding-left:12px;position:relative}
.svc-list li::before{content:"‹";position:absolute;left:0;color:var(--red);font-weight:700}
.testi-box{left:98px;top:638px;width:140px;height:94px;background:var(--red);color:#fff;padding:8px}
.testi-box h4{font-size:8.5px}
.testi-box p{font-size:7.4px;line-height:10.4px;margin-top:7px;padding-left:3px}
.video{width:112px;height:92px;background:#000;border:1px solid #3b8fd6}
.video .play{position:absolute;left:46px;top:36px;width:20px;height:14px;background:#666;border-radius:3px}
.video .play::after{content:"";position:absolute;left:8px;top:3px;border-left:6px solid #ddd;border-top:4px solid transparent;border-bottom:4px solid transparent}
.video .bar{position:absolute;left:0;bottom:0;width:100%;height:6px;background:#2a5fa8}
.caption{font-size:7px;color:var(--red)}
.arrow-btn{width:10px;height:10px;background:var(--red)}
.lower{left:0;top:774px;width:754px;height:224px;background:var(--light-bg);border-top:1px solid #d5d5d5}
.date{width:40px;height:42px;background:var(--red);color:#fff;text-align:center;font-size:7px;padding-top:6px;line-height:8px}
.date b{display:block;font-size:15px;font-weight:400;line-height:16px}
.news-text{width:122px;font-size:7.4px;line-height:11.6px}
.folio{left:320px;top:813px;width:133px;height:159px;background:linear-gradient(#3c4a2a 0 40%,#fff 40%)}
.form-label{font-size:7.4px}
.field{width:108px;height:15px;background:#fff;border:1px solid #ccc}
.star{color:var(--red);font-size:7px}
.strip{left:0;top:998px;width:754px;height:72px;background:var(--beige)}
.strip h5{font-size:8.5px;color:var(--red)}
.strip p{font-size:7.4px;line-height:12px;color:#333}
.more{font-size:7.4px;color:var(--red);text-decoration:underline}
.ph{background:#b89a66;border-radius:4px}
.footer{left:0;top:1070px;width:754px;height:103px;background:var(--red)}
.footer h6{font-size:8.5px;color:#fff}
.flink{font-size:7px;color:var(--link-gold);line-height:14px}
.flink b{color:#fff;font-weight:400}
.flink::before{content:"›";color:#fff;margin-right:10px}
.sq{display:inline-block;width:8px;height:8px;background:#2a6fc0;margin-right:8px;vertical-align:-1px}
.bottom{left:0;top:1173px;width:754px;height:27px;background:var(--footer-dark);color:#d8b86a;font-size:7px;padding:9px 0 0 98px}
</style>
</head>
<body>
<div class="abs topline"></div>
<div class="abs brand"><span class="brand-dot"></span><span class="brand-name">Plorven</span></div>
<div class="abs quote-btn">REQUEST A FREE QUOTE<span></span></div>
<div class="abs socials"><i></i><i></i><i></i><i></i><i></i><i></i></div>

<nav class="abs nav">
  <a class="active" style="left:103px">HOME</a><b style="left:143px"></b>
  <a style="left:160px">ABOUT US</a><b style="left:215px"></b>
  <a style="left:234px">SERVICES</a><b style="left:285px"></b>
  <a style="left:302px">BLOG</a><b style="left:341px"></b>
  <a style="left:358px">TESTIMONIALS</a><b style="left:431px"></b>
  <a style="left:448px">RESOURCES</a><b style="left:509px"></b>
  <a style="left:526px">PORTFOLIO</a><b style="left:586px"></b>
  <a style="left:603px">CONTACT US</a>
</nav>

<section class="abs hero" role="img" aria-label="Dark blue blueprint drawing background">
  <h1 class="abs">WHAT WE DO ??</h1>
  <p class="abs">Lorem Ipsum is simply dummy text of the printing and typesetting industry. Lorem Ipsum has been the industry's standard dummy text ever since the 1500s, when an unknown printer took a galley of type and scrambled it to make a type specimen book. It has survived not only five centuries, but also the leap into electronic typesetting, remaining essentially unchanged.</p>
  <div class="abs btn-red" style="left:101px;top:181px;width:89px;height:25px">READ MORE</div>
  <div class="abs tablet">
    <div class="abs screen" role="img" aria-label="Blue puzzle piece photo labelled web development"></div>
    <div class="abs dots"><i></i><i></i><i></i></div>
  </div>
</section>

<div class="abs card" style="left:98px"><h3>Social Media Marketing</h3><p>Lorem Ipsum is simply dummy text of the printing and typesetting industry. Lorem Ipsum has been the industry's standard dummy text ever since the 1500s, when an unknown print-</p><span class="tag hot">Read More</span></div>
<div class="abs card" style="left:240px"><h3>Web Designing</h3><p>Lorem Ipsum is simply dummy text of the printing and typesetting industry. Lorem Ipsum has been the industry's standard dummy text ever since the 1500s, when an unknown print-</p><span class="tag">Read More</span></div>
<div class="abs card" style="left:382px"><h3>S.E.O Services</h3><p>Lorem Ipsum is simply dummy text of the printing and typesetting industry. Lorem Ipsum has been the industry's standard dummy text ever since the 1500s, when an unknown print-</p><span class="tag">Read More</span></div>
<div class="abs card" style="left:524px"><h3>Domine Registration</h3><p>Lorem Ipsum is simply dummy text of the printing and typesetting industry. Lorem Ipsum has been the industry's standard dummy text ever since the 1500s, when an unknown print-</p><span class="tag">Read More</span></div>

<div class="abs side-panel"></div>
<div class="abs sec-title" style="left:98px;top:505px">Our Services</div>
<ul class="abs svc-list">
  <li>Mobile App Developmenat</li><li>Internet Marketing</li><li>Social media Marketing</li>
  <li>Serch Engine Optimization</li><li>Domine Name Registration</li><li>Web site Designing</li>
</ul>
<div class="abs testi-box">
  <h4>TESTIMONIALS <span style="float:right;font-weight:400">‹ ›</span></h4>
  <p>"Dr Ravel says : Ipsum is simply dummy text of the printing and typesetting industry. Lorem Ipsum has been the industry's standard dummy text ever since the 1500s,"</p>
</div>

<div class="abs sec-title" style="left:294px;top:505px">Customer Testimonials and Our Services</div>
<div class="abs video" style="left:294px;top:521px"><span class="play"></span><span class="bar"></span></div>
<div class="abs video" style="left:418px;top:521px"><span class="play"></span><span class="bar"></span></div>
<div class="abs video" style="left:542px;top:521px"><span class="play"></span><span class="bar"></span></div>
<div class="abs caption" style="left:294px;top:618px">Our clients says that..!</div>
<div class="abs caption" style="left:418px;top:618px">Our latest services. !</div>
<div class="abs caption" style="left:542px;top:618px">Our Suprting team. !</div>
<div class="abs video" style="left:294px;top:638px"><span class="play"></span><span class="bar"></span></div>
<div class="abs video" style="left:418px;top:638px"><span class="play"></span><span class="bar"></span></div>
<div class="abs video" style="left:542px;top:638px"><span class="play"></span><span class="bar"></span></div>
<div class="abs caption" style="left:293px;top:735px">Our SMM services..!</div>
<div class="abs caption" style="left:417px;top:735px">Our web designing. !</div>
<div class="abs caption" style="left:543px;top:735px">Register a Domine. !</div>
<div class="abs arrow-btn" style="left:629px;top:748px"></div>
<div class="abs arrow-btn" style="left:645px;top:748px"></div>

<section class="abs lower"></section>
<div class="abs sec-title" style="left:99px;top:796px">Latest News &amp; Events</div>
<div class="abs date" style="left:98px;top:817px">FEB<b>5</b></div>
<div class="abs news-text" style="left:147px;top:815px">Lorem Ipsum is simply dummy text of the printing and typesetting industry. Lorem Ipsum has been the industry's standard dummy text</div>
<div class="abs date" style="left:98px;top:874px">FEB<b>8</b></div>
<div class="abs news-text" style="left:147px;top:872px">Transfer sheets containing Lorem Ipsum passages, and more recently with desktop publishing software like Folio LayoutPro including</div>
<div class="abs date" style="left:98px;top:931px">FEB<b>9</b></div>
<div class="abs news-text" style="left:147px;top:929px">printing and typesetting industry. Lorem Ipsum has been the industry's standard dummy text ever since the 1500s, when an unknown</div>

<div class="abs sec-title" style="left:320px;top:796px">Our Portfoliyo</div>
<div class="abs arrow-btn" style="left:428px;top:796px"></div>
<div class="abs arrow-btn" style="left:444px;top:796px"></div>
<div class="abs folio" role="img" aria-label="Screenshot of an interior design website in green and white"></div>

<div class="abs sec-title" style="left:501px;top:796px">Request a Free Quote</div>
<div class="abs form-label" style="left:504px;top:815px">Name</div><div class="abs field" style="left:546px;top:811px"></div>
<div class="abs form-label" style="left:504px;top:836px">E-mail</div><span class="abs star" style="left:534px;top:834px">*</span><div class="abs field" style="left:546px;top:832px"></div>
<div class="abs form-label" style="left:504px;top:857px">Phone</div><span class="abs star" style="left:534px;top:855px">*</span><div class="abs field" style="left:546px;top:853px"></div>
<div class="abs form-label" style="left:504px;top:878px">Service</div><span class="abs star" style="left:534px;top:876px">*</span>
<div class="abs field" style="left:546px;top:874px;font-size:7px;color:var(--red);padding:3px 0 0 5px">Web designing<span class="abs" style="right:0;top:0;width:15px;height:13px;background:var(--red)"></span></div>
<div class="abs form-label" style="left:504px;top:899px">Message</div><span class="abs star" style="left:535px;top:897px">*</span>
<div class="abs field" style="left:546px;top:893px;height:51px"></div>
<div class="abs btn-red" style="left:594px;top:952px;width:60px;height:18px">Submit</div>

<section class="abs strip">
  <div class="abs ph" style="left:100px;top:10px;width:48px;height:34px;background:#b3a27a" role="img" aria-label="Chat bubbles icon"></div>
  <h5 class="abs" style="left:157px;top:12px">FROM OUR BLOG</h5>
  <p class="abs" style="left:157px;top:26px;width:115px">If you are interested in what we are talking about now.</p>
  <span class="abs more" style="left:248px;top:53px">More</span>
  <div class="abs ph" style="left:302px;top:13px;width:32px;height:38px" role="img" aria-label="Clipboard icon"></div>
  <h5 class="abs" style="left:342px;top:12px">REQUEST A QUOTE</h5>
  <p class="abs" style="left:342px;top:27px;width:115px">If you'd like some fresh ideas or would like to discuss a project.</p>
  <span class="abs more" style="left:428px;top:54px">More</span>
  <div class="abs ph" style="left:482px;top:13px;width:40px;height:38px;background:#7a4a32" role="img" aria-label="Vintage telephone icon"></div>
  <h5 class="abs" style="left:531px;top:12px">FREE SPEECH</h5>
  <p class="abs" style="left:534px;top:27px;width:120px">If you'd like to talk to someone about our business and services, please call : <span style="color:var(--red);font-size:9.5px">555-014-2287</span></p>
</section>

<footer class="abs footer">
  <div class="abs ph" style="left:102px;top:10px;width:24px;height:22px;background:#e8b340;border-radius:50%" role="img" aria-label="Globe icon"></div>
  <h6 class="abs" style="left:134px;top:22px">EXPLORE</h6>
  <div class="abs" style="left:98px;top:37px">
    <div class="flink">What we're all <b>About</b></div><div class="flink"><b>The Services</b> we offer</div>
    <div class="flink">Some of our <b>best Work</b></div><div class="flink"><b>Clients</b> we work with</div>
  </div>
  <div class="abs" style="left:198px;top:37px">
    <div class="flink">Read our <b>Blog</b></div><div class="flink">How to <b>Contact us</b></div>
    <div class="flink"><b>Terms</b> &amp; Conditions</div><div class="flink"><b>Privacy</b> Policy</div>
  </div>
  <div class="abs ph" style="left:346px;top:8px;width:26px;height:26px;background:#3d3d3d" role="img" aria-label="Smartphone icon"></div>
  <h6 class="abs" style="left:383px;top:22px">GET IN TOUCH</h6>
  <div class="abs" style="left:353px;top:37px">
    <div class="flink" style="line-height:14px"><span class="sq"></span>Connect with <b>Linkwise</b></div>
    <div class="flink"><span class="sq"></span>Connect with <b>Chirper</b></div>
    <div class="flink"><span class="sq"></span>Connect with <b>Facebloc</b></div>
    <div class="flink"><span class="sq"></span>Connect with <b>Globe+</b></div>
  </div>
  <div class="abs ph" style="left:524px;top:6px;width:26px;height:24px;background:#f0c04a" role="img" aria-label="Envelope icon"></div>
  <h6 class="abs" style="left:558px;top:22px">SUBSCRIBE NEWSLETTER</h6>
  <div class="abs field" style="left:527px;top:44px;width:127px;height:16px;font-size:7px;padding:3px 0 0 12px">E-mail address</div>
  <div class="abs" style="left:594px;top:74px;width:60px;height:17px;background:#f3ead8;border-radius:3px;font-size:8.5px;text-align:center;line-height:17px">Subscribe</div>
</footer>
<div class="abs bottom">2013@ Allright Reserved by Plorven</div>
</body>
</html>
```